"Thank You" card for professional property management agency.

We need to create a DL size "Thank You" card primarily used to thank new clients for their business and referrals.
We are a real estate agency based on Sydney's Northern Beaches. We want the card to feel happy and professional, incorporating our logo.
See our website for details about our business - www.harbourlanerealty.com.au
We have attached our logo in black text and white text as well as some images we have used across our website.
One side must have the ability to hand write a message of thank you on.
I would like this to be a clean and simple design, feel free to use any image supplied, but we are also happy with plain or patterned designs too.

Target Market(s)

Property investors male and female aged 30-60

Industry/Entity Type

Real Estate

Font styles to use
Other font styles liked:
• Please let the designer choose font

Colors

Designer to choose colors to be used in the design.

Requirements
Must have
• DL Size: Full Bleed 213x102mm. Doc size 210x99mm (horizontal)
• Harbour Lane Realty Logo
• Contact Details:
• info@harbourlanerealty.com.au
• Tel: 0493 716 258
• Suite 3, 17 Wentmore Rd, Calderwood TAS 7010
• "Thank You" somewhere on the card
• Area or side to write message on.
• Design to be provided in editable photoshop PSD file and print ready PDF file
Nice to have
• Sleek professional design that feels "happy or grateful" as it is a thank you card
• Happy to use a plain colour or pattern on one side - it does not have to be an image provided, but feel free to design with either.
Should not have
• should not be too busy, keep it clean and simple.

```html
<!DOCTYPE html>
<html lang="en">
<head>
<meta charset="utf-8">
<title>Harbour Lane Realty – Thank You Card</title>
<link href="https://fonts.googleapis.com/css2?family=Dancing+Script:wght@600&family=Lato:wght@400;900&display=swap" rel="stylesheet">
<style>
  :root {
    --bg: #e9e9e9;
    --paper: #ffffff;
    --gold: #c9a45a;
    --gold-light: #f3e6c6;
    --ink: #1a1a1a;
    --teal: #2f8a94;
    --rule: #b9b9b9;
  }
  * { box-sizing: border-box; margin: 0; padding: 0; }
  html, body { width: 1200px; height: 800px; overflow: hidden; }
  body {
    background: var(--bg);
    font-family: "Lato", sans-serif;
    color: var(--ink);
    position: relative;
  }
  .card {
    position: absolute;
    left: 250px;
    width: 700px;
    height: 330px;
    background: var(--paper);
    box-shadow: 0 6px 18px rgba(0,0,0,0.12);
    overflow: hidden;
  }
  .card--message { top: 40px; }
  .card--contact { top: 430px; }

  .pattern-fill {
    position: absolute;
    inset: 0;
    background:
      radial-gradient(circle at 30% 60%, var(--gold-light) 0%, rgba(243,230,198,0) 45%),
      radial-gradient(circle at 75% 30%, var(--gold-light) 0%, rgba(243,230,198,0) 40%),
      linear-gradient(135deg, #fbf6ea 0%, #f5ead0 50%, #fbf6ea 100%);
  }

  /* Message side */
  .message-panel {
    position: absolute;
    left: 30px; top: 26px; right: 30px; bottom: 26px;
    background: var(--paper);
    border: 2px solid var(--gold);
    outline: 6px solid var(--paper);
  }
  .thank-you {
    position: absolute;
    top: 14px; right: 24px;
    font-family: "Dancing Script", cursive;
    font-weight: 600;
    font-size: 30px;
    color: var(--gold);
  }
  .writing-lines {
    position: absolute;
    left: 30px; right: 30px; top: 58px;
  }
  .writing-lines li {
    list-style: none;
    height: 24px;
    border-bottom: 1px dashed var(--rule);
  }
  .brand-small {
    position: absolute;
    left: 18px; bottom: 12px;
    display: flex; align-items: center; gap: 6px;
    font-weight: 900;
    font-size: 11px;
    letter-spacing: 0.02em;
    text-transform: uppercase;
    white-space: nowrap;
  }
  .brand-mark {
    display: inline-block;
    flex: none;
    background: var(--teal);
  }
  .brand-small .brand-mark { width: 9px; height: 9px; }

  /* Contact side */
  .contact-panel {
    position: absolute;
    right: 36px; top: 34px;
    width: 262px; height: 214px;
    background: var(--paper);
    border: 2px solid var(--gold);
    outline: 5px solid var(--paper);
    padding: 34px 20px 18px;
    text-align: right;
  }
  .brand-name {
    display: flex; align-items: center; justify-content: flex-end; gap: 8px;
    font-weight: 900;
    font-size: 18px;
    text-transform: uppercase;
    letter-spacing: 0.01em;
    white-space: nowrap;
    margin-bottom: 34px;
  }
  .brand-name .brand-mark { width: 13px; height: 13px; }
  .contact-details {
    font-style: normal;
    font-size: 11.5px;
    line-height: 1.55;
  }
  .contact-details .email { margin-top: 12px; }
</style>
</head>
<body>

  <section class="card card--message" aria-label="Message side">
    <div class="pattern-fill" role="img" aria-label="Gold geometric line pattern border"></div>
    <div class="message-panel">
      <p class="thank-you">Thank You</p>
      <ul class="writing-lines">
        <li></li><li></li><li></li><li></li><li></li><li></li><li></li>
      </ul>
      <p class="brand-small"><span class="brand-mark"></span>Harbour Lane Realty</p>
    </div>
  </section>

  <section class="card card--contact" aria-label="Contact side">
    <div class="pattern-fill" role="img" aria-label="Gold geometric star line pattern on white"></div>
    <div class="contact-panel">
      <p class="brand-name"><span class="brand-mark"></span>Harbour Lane Realty</p>
      <address class="contact-details">
        <p>Suite 3, 17 Wentmore Rd</p>
        <p>Calderwood TAS 7010</p>
        <p>Tel: 0493 716 258</p>
        <p class="email">info@harbourlanerealty.com.au</p>
      </address>
    </div>
  </section>

</body>
</html>
```